Alder Bay community splash page

We need an elegant splash page with minimal information for a lake development project that will open next summer. You can see what we currently use at www.alder-bay.example. Most of the existing information needs to be on the splash page.

Target Market(s)

People who are interested in purchasing lots at our lake community. Up scale housing on a private lake with marinas.

Industry/Entity Type

Community

Coding

Coded - Design and coding required

Requirements
Must have
• Must have contact information for Alder Development LLC. Must have link to marketing plat file.
Nice to have
• Would be nice to have linking capability to prezi tour file already created. See tour here: http://slidetrek.example/qmvvtr7wk2pl/?utm_campaign=share&utm_medium=copy&rc=ex0share
Should not have
• We want this standout, not be conservative or traditional. Must be elegant and bold.

```html
<!DOCTYPE html>
<html lang="en">
<head>
<meta charset="utf-8">
<title>Alder Bay — Alder Development</title>
<link href="https://fonts.googleapis.com/css2?family=Mulish:wght@600;700&family=Arimo:wght@400;700&display=swap" rel="stylesheet">
<style>
  :root {
    --sky-top: #a9d6f3;
    --sky-mid: #dceefa;
    --tree-band: #8a9a62;
    --water-light: #7d98bf;
    --water-deep: #2c4b86;
    --panel: rgba(255, 255, 255, 0.55);
    --navy: #143a70;
    --brand: #0f3f7c;
    --frame: #ffffff;
    --frame-active: #0a780a;
    --button-top: #1a4f93;
    --button-bottom: #062a5e;
    --footer-text: #ffffff;
  }
  * { box-sizing: border-box; margin: 0; padding: 0; }
  html, body { width: 1200px; height: 780px; overflow: hidden; }
  body { position: relative; font-family: "Mulish", sans-serif; }

  .lake-backdrop {
    position: absolute; inset: 0;
    background: linear-gradient(180deg,
      var(--sky-top) 0%, var(--sky-mid) 30%, #eef6fb 42%,
      var(--tree-band) 48%, #9aa97a 56%,
      var(--water-light) 62%, #5877aa 78%, var(--water-deep) 100%);
  }

  .brand {
    position: absolute; top: 62px; left: 0; width: 1200px;
    text-align: center;
    font-family: "Mulish", sans-serif; font-weight: 700;
    font-size: 34px; letter-spacing: 6px; color: var(--brand);
  }

  .welcome-panel {
    position: absolute; left: 98px; top: 153px; width: 1004px; height: 507px;
    background: var(--panel);
  }
  .welcome-title {
    position: absolute; top: 24px; left: 0; width: 100%;
    text-align: center; color: var(--navy);
    font-weight: 700; font-size: 34px; line-height: 48px; letter-spacing: 1.6px;
  }

  .gallery-photo {
    position: absolute; top: 146px; width: 250px; height: 220px;
    border: 9px solid var(--frame); display: block;
  }
  .gallery-photo.is-active { border: 10px solid var(--frame-active); }
  .photo-fill { width: 100%; height: 100%; }
  .photo-one { left: 84px; }
  .photo-one .photo-fill { background: linear-gradient(180deg, #3d95e0 0%, #8ec4ee 38%, #3e6a3a 46%, #2b5a95 60%, #163468 100%); }
  .photo-two { left: 374px; }
  .photo-two .photo-fill { background: linear-gradient(180deg, #7d8ea8 0%, #e8a39a 22%, #45453a 30%, #c9c6cf 55%, #9a8f86 80%, #3f3a2e 100%); }
  .photo-three { left: 669px; }
  .photo-three .photo-fill { background: linear-gradient(180deg, #3f9ae6 0%, #9cc8ef 38%, #4f6a2f 55%, #3259a0 65%, #20407c 100%); }

  .download-button {
    position: absolute; left: 254px; top: 412px; width: 497px; height: 55px;
    border-radius: 4px;
    background: linear-gradient(180deg, var(--button-top), var(--button-bottom));
    color: #fff; text-decoration: none;
    font-family: "Mulish", sans-serif; font-weight: 700; font-size: 20px;
    display: flex; align-items: center; justify-content: center;
  }

  .site-footer {
    position: absolute; top: 707px; left: 0; width: 1200px;
    text-align: center; color: var(--footer-text);
    font-family: "Arimo", sans-serif; font-size: 14px; line-height: 24px;
    text-shadow: 0 1px 2px rgba(0, 0, 0, 0.55);
  }
  .site-footer a { color: inherit; text-decoration: none; }
</style>
</head>
<body>
  <div class="lake-backdrop" role="img" aria-label="Wide photo of a calm lake with tree-lined shore under a pale blue sky"></div>

  <div class="brand">ALDER DEVELOPMENT</div>

  <main class="welcome-panel">
    <h1 class="welcome-title">Thank you for your interest in Alder Bay<br>Click on the black triangle below to start your tour</h1>

    <a class="gallery-photo photo-one is-active" href="http://slidetrek.example/qmvvtr7wk2pl/?utm_campaign=share&amp;utm_medium=copy&amp;rc=ex0share">
      <div class="photo-fill" role="img" aria-label="Lake view framed by overhanging branches on a clear day"></div>
    </a>
    <div class="gallery-photo photo-two">
      <div class="photo-fill" role="img" aria-label="Sunset over still water with reeds in the foreground"></div>
    </div>
    <div class="gallery-photo photo-three">
      <div class="photo-fill" role="img" aria-label="Open lake with a wooded island under a blue sky"></div>
    </div>

    <a class="download-button" href="#">Click here to download a marketing sheet.</a>
  </main>

  <footer class="site-footer">
    Alder Development LLC | 1280 Shoreline Rd, Suite C | Millbrook, Indiana 46000 | &nbsp;All rights reserved ©2013-2014<br>
    <a href="mailto:info@AlderDev.example">info@AlderDev.example</a> | +1.555.010.0142
  </footer>
</body>
</html>
```